Business Card Design

Personal training company in the fitness industry

Industry/Entity Type

Training

Contact Information for Business Card

(Front of card)
Peak Hour Fitness
417 Wexley Road Brannock Vale 6172 (Inside IronHaus365 complex)
Dario Halvorsen
Personal Trainer
halvdario@mailora.net
0412 903 548
Back of card
One on One Training
Group Training (min 3)
Outdoor bootcamps
Workout programs
Meal guides
Competition preparation
(bottom middle of card)
PUT IN THE WORK!

```html
<!DOCTYPE html>
<html lang="en">
<head>
<meta charset="utf-8">
<title>Peak Hour Fitness – Business Card</title>
<link rel="stylesheet" href="https://fonts.googleapis.com/css2?family=Open+Sans:wght@400;600&family=Share+Tech+Mono&display=swap">
<style>
  :root {
    --page-bg: #3a2c36;
    --card-black: #000000;
    --brand-blue: #4c9fe0;
    --brand-red: #ec1c24;
    --title-gold: #e8a417;
    --text-white: #ffffff;
    --divider-grey: #6b6b6b;
  }
  * { box-sizing: border-box; margin: 0; padding: 0; }
  html, body { width: 1200px; height: 800px; overflow: hidden; }
  body {
    background: var(--page-bg);
    font-family: "Open Sans", sans-serif;
    color: var(--text-white);
    display: flex;
    align-items: center;
    justify-content: center;
    gap: 40px;
  }
  .card {
    width: 540px;
    height: 309px;
    background: var(--card-black);
    position: relative;
    overflow: hidden;
    box-shadow: 0 10px 30px rgba(0,0,0,0.45);
  }
  .brand {
    display: flex;
    align-items: center;
    gap: 10px;
    font-weight: 600;
    color: var(--brand-blue);
    white-space: nowrap;
  }
  .brand-dot {
    width: 22px; height: 22px;
    border-radius: 50%;
    background: var(--brand-blue);
    flex: none;
  }

  /* Back of card: services */
  .card-back .brand {
    position: absolute;
    top: 70px; left: 0; right: 0;
    justify-content: center;
    font-size: 30px;
  }
  .services {
    position: absolute;
    top: 150px; left: 0; right: 0;
    text-align: center;
    font-size: 15px;
    line-height: 24px;
  }
  .slogan-band {
    position: absolute;
    left: 0; right: 0; bottom: 22px;
    height: 44px;
    background: var(--brand-red);
    display: flex;
    align-items: center;
    justify-content: center;
  }
  .slogan {
    font-family: "Share Tech Mono", monospace;
    font-size: 20px;
    letter-spacing: 3px;
    color: var(--text-white);
  }

  /* Front of card: contact */
  .card-front .brand {
    position: absolute;
    top: 138px; left: 30px;
    font-size: 23px;
  }
  .divider {
    position: absolute;
    left: 282px; top: 60px;
    width: 1px; height: 190px;
    background: var(--divider-grey);
  }
  .contact {
    position: absolute;
    left: 302px; top: 84px;
    right: 14px;
  }
  .person-name { font-size: 22px; font-weight: 400; line-height: 28px; }
  .person-title { font-size: 14px; color: var(--title-gold); margin-bottom: 10px; }
  .address { font-size: 12px; line-height: 17px; margin-bottom: 6px; }
  .contact-line { display: flex; align-items: center; gap: 7px; font-size: 12px; line-height: 19px; }
  .contact-icon { width: 11px; height: 11px; flex: none; }
</style>
</head>
<body>

  <section class="card card-back" aria-label="Back of card">
    <div class="brand"><span class="brand-dot"></span>Peak Hour Fitness</div>
    <div class="services">
      <p>One on One Training | Group Training (min 3) | Outdoor bootcamps</p>
      <p>Workout programs | Meal guides | Competition preparation</p>
    </div>
    <div class="slogan-band"><span class="slogan">PUT IN THE WORK!</span></div>
  </section>

  <section class="card card-front" aria-label="Front of card">
    <div class="brand"><span class="brand-dot"></span>Peak Hour Fitness</div>
    <div class="divider"></div>
    <div class="contact">
      <h1 class="person-name">Dario Halvorsen</h1>
      <p class="person-title">Personal Trainer</p>
      <p class="address">417 Wexley Road Brannock Vale 6172<br>(Inside IronHaus365 complex)</p>
      <p class="contact-line">
        <svg class="contact-icon" viewBox="0 0 12 12"><rect width="12" height="12" rx="2" fill="#ec1c24"/><path d="M3.2 2.6c.4-.3.8-.2 1 .2l.6 1.2c.2.4 0 .7-.3.9l-.4.3c.4 1 1.1 1.7 2 2.1l.3-.4c.2-.3.6-.4.9-.2l1.2.6c.4.2.5.6.2 1l-.5.6c-.4.4-1 .5-1.6.2C4.9 8.3 3.7 7.1 2.9 5.4c-.3-.6-.2-1.2.3-1.6z" fill="#fff"/></svg>
        0412 903 548
      </p>
      <p class="contact-line">
        <svg class="contact-icon" viewBox="0 0 12 12"><rect width="12" height="12" rx="2" fill="#ec1c24"/><rect x="2.2" y="3.4" width="7.6" height="5.2" fill="none" stroke="#fff" stroke-width="1"/><path d="M2.2 3.4 6 6.4l3.8-3" fill="none" stroke="#fff" stroke-width="1"/></svg>
        halvdario@mailora.net
      </p>
    </div>
  </section>

</body>
</html>
```